business card for a shoe shop

we would like a business card for a family owned shoe shop.
With this information included.
Dunleavy's Shoe Store
Family owned since 1947

then on other side
Dunleavy's Shoe Store
Footwear fitting specialist
Phone: 9471 2386
218 Tarn St, Wexley Heights 3091
(cnr. Corrigan Rd and Tarn St)
dunleavyshoes218@quillmail.example
if could incorporate the purple color on card i have attached.

```html
<!DOCTYPE html>
<html lang="en">
<head>
<meta charset="utf-8">
<title>Dunleavy's Shoe Store – Business Card</title>
<link rel="stylesheet" href="https://fonts.googleapis.com/css2?family=Arimo:wght@400&display=swap">
<style>
  :root {
    --brand-purple: #7459a8;
    --text-grey: #676767;
    --card-white: #ffffff;
    --backdrop: #e4e4e6;
  }
  * { margin: 0; padding: 0; box-sizing: border-box; }
  html, body {
    width: 1200px; height: 1200px; overflow: hidden;
    background: var(--backdrop);
    font-family: "Arimo", Arial, sans-serif;
  }
  .canvas { position: relative; width: 1200px; height: 1200px; }
  .card {
    position: absolute; top: 480px;
    width: 420px; height: 240px;
    border-radius: 19px; overflow: hidden;
  }
  .card--front { left: 155px; background: var(--card-white); }
  .card--back { left: 623px; background: var(--brand-purple); }

  .brand-name {
    display: flex; align-items: center; gap: 7px;
    font-size: 20px; font-weight: 400; white-space: nowrap;
  }
  .brand-name__dot {
    width: 10px; height: 10px; border-radius: 50%;
    background: currentColor; flex: none;
  }
  .card--front .brand-name {
    position: absolute; left: 17px; top: 30px;
    color: var(--brand-purple);
  }
  .card--back .brand-name {
    position: absolute; left: 0; right: 0; top: 98px;
    justify-content: center; color: var(--card-white); font-size: 23px;
  }
  .heritage-line {
    position: absolute; left: 0; right: 0; top: 134px;
    text-align: center; color: var(--card-white);
    font-size: 11.5px; letter-spacing: 4px; text-transform: uppercase;
    white-space: nowrap;
  }

  .tagline {
    position: absolute; left: 16px; top: 120px;
    font-size: 16px; color: var(--text-grey);
  }
  .tagline-rule {
    position: absolute; left: 204px; right: 0; top: 136px;
    height: 1px; background: var(--brand-purple);
  }
  .contact-list {
    position: absolute; left: 17px; top: 155px;
    list-style: none; font-size: 12.5px; color: var(--text-grey);
  }
  .contact-list li { display: flex; align-items: center; gap: 5px; height: 15px; }
  .contact-list svg { width: 11px; height: 11px; flex: none; fill: var(--brand-purple); }
  .address {
    position: absolute; left: 17px; top: 198px;
    font-size: 12.5px; line-height: 15px; color: var(--text-grey);
    font-style: normal;
  }
</style>
</head>
<body>
<main class="canvas">
  <section class="card card--front" aria-label="Business card front">
    <div class="brand-name"><span class="brand-name__dot"></span>Dunleavy's Shoe Store</div>
    <p class="tagline">Footwear fitting specialist</p>
    <div class="tagline-rule"></div>
    <ul class="contact-list">
      <li>
        <svg viewBox="0 0 24 24" aria-hidden="true"><path d="M6.6 10.8a15.1 15.1 0 0 0 6.6 6.6l2.2-2.2a1 1 0 0 1 1-.25 11.4 11.4 0 0 0 3.6.57 1 1 0 0 1 1 1V20a1 1 0 0 1-1 1A17 17 0 0 1 3 4a1 1 0 0 1 1-1h3.5a1 1 0 0 1 1 1c0 1.25.2 2.45.57 3.57a1 1 0 0 1-.25 1z"/></svg>
        9471 2386
      </li>
      <li>
        <svg viewBox="0 0 24 24" aria-hidden="true"><path d="M2 5h20v14H2zm2 2v.4l8 5.2 8-5.2V7zm0 2.8V17h16V9.8l-8 5.2z"/></svg>
        dunleavyshoes218@quillmail.example
      </li>
    </ul>
    <address class="address">
      218 Tarn St, Wexley Heights 3091<br>
      (cnr. Corrigan Rd and Tarn St)
    </address>
  </section>

  <section class="card card--back" aria-label="Business card back">
    <div class="brand-name"><span class="brand-name__dot"></span>Dunleavy's Shoe Store</div>
    <p class="heritage-line">Family owned since 1947</p>
  </section>
</main>
</body>
</html>
```